PowerPoint Template for Consultancy Company.

We need a Power Point template for a Consultancy company based in Copenhagen, Denmark. We focus on supporting people and small companies in starting up next generation technology companies. Company name is "Vorbek-Halstrup Consulting". The template shall demonstrate growth, agility, next generation technology and following your dreams. Please include the uploaded logo.
Updates
Hi guys,
thanks for helping me on this project.
I like the font "Good Times" that is being used in my logo. I will like this to be used as minimum in the headlines in my power point template. I am not sure if it will work on standard text - but will relay on your judgement.
Kind regards
Torvald
Colors
Designer to choose colors to be used in the design.
Look and feel
Each slider illustrates characteristics of the customer's brand and the style your logo design should communicate.

```html
<!DOCTYPE html>
<html lang="en">
<head>
<meta charset="utf-8">
<title>Vorbek-Halstrup Consulting – Slide Template Overview</title>
<link rel="stylesheet" href="https://fonts.googleapis.com/css2?family=Michroma&family=Open+Sans:wght@400;600;700&display=swap">
<style>
:root{
  --canvas:#9c9c9c;
  --red:#e2352c;
  --red-dark:#a3221c;
  --navy:#2b2667;
  --navy-deep:#221d58;
  --ink:#4a4a4a;
  --muted:#8a8a8a;
  --paper:#ffffff;
  --chip:#e4e4e4;
}
*{margin:0;padding:0;box-sizing:border-box}
html,body{width:1200px;height:1074px;overflow:hidden;background:var(--canvas)}
.board{position:relative;width:1200px;height:1074px}
.slide{position:absolute;width:241px;height:136px;background:var(--paper);overflow:hidden;box-shadow:0 1px 3px rgba(0,0,0,.25)}
.abs{position:absolute}
.photo{position:absolute;background:linear-gradient(135deg,#8f97a6,#c9ccd3 55%,#6f7787)}
.photo.warm{background:linear-gradient(135deg,#6e5c52,#c6b3a3 50%,#3f3c45)}
.photo.sky{background:linear-gradient(180deg,#7fa6cf,#c8d7e6 45%,#5c6a5a)}
.photo.city{background:linear-gradient(180deg,#3b4a78,#7d6f8c 50%,#d39a5a 75%,#3a3a44)}
.photo.office{background:linear-gradient(135deg,#b9b7b1,#e3e1dc 50%,#7f8784)}
.photo.navytint{background:linear-gradient(135deg,#2b2667,#4a4f8a 50%,#2b2667)}
.photo.redtint{background:linear-gradient(135deg,#b8261f,#e2352c 50%,#c22d25)}
.photo.round{border-radius:50%}
.h{font-family:'Michroma',sans-serif;font-size:7.2px;letter-spacing:.2px;color:var(--navy);text-transform:uppercase;white-space:nowrap}
.h.white{color:#fff}
.h.big{font-size:11px}
.lead{font-family:'Open Sans',sans-serif;font-weight:600;font-size:6px;line-height:1.3;color:var(--navy)}
.lead.white{color:#fff}
.copy{font-family:'Open Sans',sans-serif;font-size:3.1px;line-height:1.38;color:var(--ink)}
.copy.white{color:#f1f1f1}
.label{font-family:'Open Sans',sans-serif;font-size:3.6px;font-weight:600;color:var(--navy)}
.label.red{color:var(--red)}
.label.white{color:#fff}
.tag{position:absolute;background:var(--red);color:#fff;font-family:'Open Sans',sans-serif;font-size:3.3px;font-weight:600;padding:1px 3px}
.tag.navy{background:var(--navy)}
.quote{font-family:'Open Sans',sans-serif;font-weight:600;color:var(--navy);font-size:5.6px;line-height:1.35;text-align:center}
.quote.white{color:#fff}
.icon{position:absolute;width:11px;height:11px}
.chip{position:absolute;background:var(--chip);font-family:'Open Sans',sans-serif;font-size:2.8px;text-align:center;color:#333;line-height:1.3;padding-top:1px}
.chip b{display:block;font-size:3px}
.brand-mark{position:absolute;font-family:'Michroma',sans-serif;color:#fff;font-size:8.4px;line-height:1.35;letter-spacing:.4px}
.mini-brand{position:absolute;font-family:'Open Sans',sans-serif;font-size:2.6px;font-weight:700;color:var(--navy)}
.mini-brand i{display:inline-block;width:4px;height:4px;background:var(--navy);vertical-align:middle;margin-right:1px}
</style>
</head>
<body>
<svg width="0" height="0" style="position:absolute" aria-hidden="true">
  <defs>
    <symbol id="i-chart" viewBox="0 0 12 12"><rect x="1" y="7" width="2" height="4" fill="currentColor"/><rect x="5" y="4" width="2" height="7" fill="currentColor"/><rect x="9" y="1" width="2" height="10" fill="currentColor"/></symbol>
    <symbol id="i-doc" viewBox="0 0 12 12"><rect x="2" y="1" width="8" height="10" fill="none" stroke="currentColor" stroke-width="1"/><path d="M4 4h4M4 6h4M4 8h3" stroke="currentColor" stroke-width=".8"/></symbol>
    <symbol id="i-people" viewBox="0 0 12 12"><circle cx="6" cy="4" r="2" fill="currentColor"/><circle cx="2.5" cy="5" r="1.4" fill="currentColor"/><circle cx="9.5" cy="5" r="1.4" fill="currentColor"/><path d="M2 11c0-3 2-4 4-4s4 1 4 4z" fill="currentColor"/></symbol>
    <symbol id="i-cal" viewBox="0 0 12 12"><rect x="1.5" y="2.5" width="9" height="8" fill="none" stroke="currentColor"/><rect x="1.5" y="2.5" width="9" height="2" fill="currentColor"/><rect x="5" y="6.5" width="2" height="2" fill="currentColor"/></symbol>
    <symbol id="i-screen" viewBox="0 0 12 12"><rect x="1" y="2" width="10" height="7" fill="none" stroke="currentColor"/><path d="M2.5 7.5l2.5-3 2 2 2.5-3" fill="none" stroke="currentColor" stroke-width=".8"/><path d="M4 11h4M6 9v2" stroke="currentColor"/></symbol>
    <symbol id="i-lock" viewBox="0 0 12 12"><rect x="2.5" y="5.5" width="7" height="5.5" fill="currentColor"/><path d="M4 5.5V4a2 2 0 0 1 4 0v1.5" fill="none" stroke="currentColor"/></symbol>
    <symbol id="i-bag" viewBox="0 0 12 12"><circle cx="6" cy="7" r="4" fill="currentColor"/><rect x="4.5" y="1.5" width="3" height="2" fill="currentColor"/></symbol>
    <symbol id="i-play" viewBox="0 0 12 12"><rect x="1" y="2" width="10" height="8" fill="none" stroke="currentColor"/><path d="M5 4.5v3l2.5-1.5z" fill="currentColor"/></symbol>
    <symbol id="i-truck" viewBox="0 0 12 12"><rect x="1" y="3" width="6" height="5" fill="currentColor"/><path d="M7 5h2.5l1.5 2v1H7z" fill="currentColor"/><circle cx="3" cy="9.5" r="1.2" fill="currentColor"/><circle cx="9" cy="9.5" r="1.2" fill="currentColor"/></symbol>
    <symbol id="i-down" viewBox="0 0 12 12"><path d="M6 1l5 5-5 5-5-5z" fill="none" stroke="currentColor"/><path d="M6 3v5M4 6l2 2 2-2" fill="none" stroke="currentColor" stroke-width=".9"/></symbol>
    <symbol id="i-quote" viewBox="0 0 12 10"><path d="M0 10V5C0 2 1.5 0 4 0v2C2.5 2 2 3 2 4.5h3V10zM7 10V5c0-3 1.5-5 4-5v2c-1.5 0-2 1-2 2.5h3V10z" fill="currentColor"/></symbol>
  </defs>
</svg>

<main class="board">

  <!-- Row 1 -->
  <section class="slide" style="left:64px;top:56px;background:var(--red)">
    <div class="photo redtint" role="img" aria-label="Red-tinted photo of a consultant working at a desk" style="inset:0;opacity:.9"></div>
    <div class="abs" style="left:60px;top:57px;width:20px;height:20px;background:#fff"></div>
    <div class="brand-mark" style="left:88px;top:56px">VORBEK-HALSTRUP<br>CONSULTING</div>
  </section>

  <section class="slide" style="left:348px;top:56px">
    <div class="photo warm" role="img" aria-label="Photo of two women collaborating at a laptop" style="left:0;top:0;width:120px;height:136px"></div>
    <div class="abs" style="left:120px;top:0;width:121px;height:136px;background:var(--navy)"></div>
    <div class="h white" style="position:absolute;left:141px;top:32px">Introduction</div>
    <p class="copy white abs" style="left:141px;top:45px;width:88px">Lorem ipsum dolor sit amet, consectetur adipiscing elit. Phasellus sodales, ligula ultrices tempus ristique, tellus justo aliquam dui, nec lorem. Lorem ipsum dolor sit amet, consectetur adipiscing elit. Phasellus sodales, ligula ultrices tempus ristique, tellus justo aliquam dui. Lorem ipsum dolor sit amet, consectetur adipiscing elit. Phasellus sodales, ligula ultrices tempus ristique, tellus justo aliquam dui, nec lorem ipsum dolor sit amet consectetur.</p>
  </section>

  <section class="slide" style="left:624px;top:56px">
    <div class="photo sky" role="img" aria-label="Photo of modern glass office buildings with trees" style="inset:0"></div>
    <div class="abs" style="left:22px;top:0;width:92px;height:115px;background:#fff"></div>
    <div class="h" style="position:absolute;left:35px;top:18px">About Us</div>
    <p class="copy abs" style="left:33px;top:32px;width:74px">Lorem ipsum dolor sit amet, consectetur adipiscing elit. Phasellus sodales, ligula ultrices tempus ristique, tellus justo aliquam dui, nec lorem. Lorem ipsum dolor sit amet, consectetur adipiscing elit. Phasellus sodales, ligula ultrices tempus ristique, tellus justo aliquam dui. Lorem ipsum dolor sit amet, consectetur adipiscing elit, sed do eiusmod tempor.</p>
  </section>

  <section class="slide" style="left:899px;top:56px">
    <div class="abs" style="left:0;top:0;width:92px;height:136px;background:var(--red)"></div>
    <div class="photo navytint" role="img" aria-label="Photo of a trading screen with city view" style="left:92px;top:0;width:149px;height:136px;opacity:.75"></div>
    <div class="h white" style="position:absolute;left:14px;top:28px;font-size:5.5px">Lorem Ipsum</div>
    <p class="copy white abs" style="left:12px;top:38px;width:50px">Lorem ipsum dolor sit amet, consectetur adipiscing elit. Phasellus sodales, ligula ultrices tempus ristique, tellus justo aliquam dui, nec lorem ipsum dolor sit amet consectetur adipiscing.</p>
    <div class="abs" style="left:70px;top:25px;width:151px;height:92px;background:#fff"></div>
    <svg class="icon" style="left:86px;top:35px;color:var(--navy)"><use href="#i-screen"/></svg>
    <div class="label abs" style="left:86px;top:49px">Lorem Ipsum</div>
    <p class="copy abs" style="left:86px;top:55px;width:50px">Lorem ipsum dolor sit amet, consectetur adipiscing elit.</p>
    <svg class="icon" style="left:156px;top:35px;color:var(--navy)"><use href="#i-doc"/></svg>
    <div class="label abs" style="left:156px;top:49px">Lorem Ipsum</div>
    <p class="copy abs" style="left:156px;top:55px;width:50px">Lorem ipsum dolor sit amet, consectetur adipiscing elit.</p>
    <svg class="icon" style="left:86px;top:77px;color:var(--navy)"><use href="#i-bag"/></svg>
    <div class="label abs" style="left:86px;top:91px">Lorem Ipsum</div>
    <p class="copy abs" style="left:86px;top:97px;width:50px">Lorem ipsum dolor sit amet, consectetur adipiscing elit.</p>
    <svg class="icon" style="left:156px;top:77px;color:var(--navy)"><use href="#i-lock"/></svg>
    <div class="label abs" style="left:156px;top:91px">Lorem Ipsum</div>
    <p class="copy abs" style="left:156px;top:97px;width:50px">Lorem ipsum dolor sit amet, consectetur adipiscing elit.</p>
  </section>

  <!-- Row 2 -->
  <section class="slide" style="left:64px;top:224px">
    <div class="h" style="position:absolute;left:15px;top:13px">Meet Our Team</div>
    <div class="photo office" role="img" aria-label="Portrait photo of a team member" style="left:15px;top:28px;width:35px;height:73px"></div>
    <div class="photo office" role="img" aria-label="Portrait photo of a team member" style="left:51px;top:28px;width:35px;height:73px"></div>
    <div class="photo office" role="img" aria-label="Portrait photo of a team member" style="left:87px;top:28px;width:35px;height:73px"></div>
    <div class="photo office" role="img" aria-label="Portrait photo of a team member" style="left:123px;top:28px;width:35px;height:73px"></div>
    <div class="photo office" role="img" aria-label="Portrait photo of a team member" style="left:159px;top:28px;width:35px;height:73px"></div>
    <div class="photo office" role="img" aria-label="Portrait photo of a team member" style="left:195px;top:28px;width:35px;height:73px"></div>
    <div class="chip" style="left:15px;top:102px;width:35px;height:13px"><b>Mikkel Ravn</b>CEO/President</div>
    <div class="chip" style="left:51px;top:102px;width:35px;height:13px"><b>Sofie Brandt</b>VP Finance</div>
    <div class="chip" style="left:87px;top:102px;width:35px;height:13px"><b>Ida Kjaer</b>Human Resource</div>
    <div class="chip" style="left:123px;top:102px;width:35px;height:13px"><b>Nora Falk</b>Managing Director</div>
    <div class="chip" style="left:159px;top:102px;width:35px;height:13px"><b>Jonas Vedel</b>Manager Delivery</div>
    <div class="chip" style="left:195px;top:102px;width:35px;height:13px"><b>Anja Holm</b>Manager Accounts</div>
  </section>

  <section class="slide" style="left:348px;top:224px">
    <div class="h" style="position:absolute;left:14px;top:13px">Our Services</div>
    <svg class="icon" style="left:16px;top:32px;color:var(--red)"><use href="#i-screen"/></svg>
    <div class="label red abs" style="left:32px;top:32px">Lorem ipsum dolor</div>
    <p class="copy abs" style="left:32px;top:37px;width:40px">Lorem ipsum dolor sit amet, consectetur adipiscing elit.</p>
    <svg class="icon" style="left:86px;top:32px;color:var(--red)"><use href="#i-doc"/></svg>
    <div class="label red abs" style="left:102px;top:32px">Lorem ipsum dolor</div>
    <p class="copy abs" style="left:102px;top:37px;width:40px">Lorem ipsum dolor sit amet, consectetur adipiscing elit.</p>
    <svg class="icon" style="left:16px;top:66px;color:var(--red)"><use href="#i-chart"/></svg>
    <div class="label red abs" style="left:32px;top:66px">Lorem ipsum dolor</div>
    <p class="copy abs" style="left:32px;top:71px;width:40px">Lorem ipsum dolor sit amet, consectetur adipiscing elit.</p>
    <svg class="icon" style="left:86px;top:66px;color:var(--red)"><use href="#i-chart"/></svg>
    <div class="label red abs" style="left:102px;top:66px">Lorem ipsum dolor</div>
    <p class="copy abs" style="left:102px;top:71px;width:40px">Lorem ipsum dolor sit amet, consectetur adipiscing elit.</p>
    <svg class="icon" style="left:16px;top:102px;color:var(--red)"><use href="#i-doc"/></svg>
    <div class="label red abs" style="left:32px;top:102px">Lorem ipsum dolor</div>
    <p class="copy abs" style="left:32px;top:107px;width:40px">Lorem ipsum dolor sit amet, consectetur adipiscing elit.</p>
    <svg class="icon" style="left:86px;top:102px;color:var(--red)"><use href="#i-people"/></svg>
    <div class="label red abs" style="left:102px;top:102px">Lorem ipsum dolor</div>
    <p class="copy abs" style="left:102px;top:107px;width:40px">Lorem ipsum dolor sit amet, consectetur adipiscing elit.</p>
    <div class="photo warm" role="img" aria-label="Photo of a smiling woman with glasses working on a laptop" style="left:160px;top:12px;width:72px;height:113px"></div>
  </section>

  <section class="slide" style="left:624px;top:224px">
    <div class="abs" style="left:0;top:0;width:98px;height:136px;background:var(--red)"></div>
    <svg class="abs" style="left:41px;top:22px;width:18px;height:15px;color:#fff"><use href="#i-quote"/></svg>
    <p class="quote white abs" style="left:12px;top:48px;width:74px;font-size:5px">“Lorem ipsum dolor sit amet, consectetur adipiscing elit. Phasellus sodales, ligula ultrices tempus ristique, tellus justo aliquam dui, nec Lorem ipsum dolor sit amet, consectetur</p>
    <div class="h" style="position:absolute;left:113px;top:10px">Testimonials</div>
    <div class="photo round" role="img" aria-label="Portrait photo of a client" style="left:113px;top:32px;width:20px;height:20px"></div>
    <div class="label abs" style="left:142px;top:32px">Lorem Ipsum</div>
    <p class="copy abs" style="left:142px;top:38px;width:88px">Lorem ipsum dolor sit amet, consectetur adipiscing elit, sed do eiusmod tempor incididunt ut labore et dolore magna aliqua.</p>
    <div class="photo round warm" role="img" aria-label="Portrait photo of a client" style="left:113px;top:66px;width:20px;height:20px"></div>
    <div class="label abs" style="left:142px;top:66px">Lorem Ipsum</div>
    <p class="copy abs" style="left:142px;top:72px;width:88px">Lorem ipsum dolor sit amet, consectetur adipiscing elit, sed do eiusmod tempor incididunt ut labore et dolore magna aliqua.</p>
    <div class="photo round warm" role="img" aria-label="Portrait photo of a client" style="left:113px;top:100px;width:20px;height:20px"></div>
    <div class="label abs" style="left:142px;top:100px">Lorem Ipsum</div>
    <p class="copy abs" style="left:142px;top:106px;width:88px">Lorem ipsum dolor sit amet, consectetur adipiscing elit, sed do eiusmod tempor incididunt ut labore et dolore magna aliqua.</p>
  </section>

  <section class="slide" style="left:899px;top:224px">
    <div class="photo office" role="img" aria-label="Photo of an open-plan office with computer workstations" style="left:0;top:0;width:110px;height:136px"></div>
    <div class="h" style="position:absolute;left:131px;top:12px">Our Portfolio</div>
    <svg class="icon" style="left:126px;top:33px;width:16px;height:16px;color:var(--navy)"><use href="#i-doc"/></svg>
    <div class="label abs" style="left:152px;top:32px">Lorem Ipsum</div>
    <p class="copy abs" style="left:152px;top:38px;width:80px">Lorem ipsum dolor sit amet, consectetur adipiscing elit, sed do eiusmod tempor incididunt ut labore et dolore.</p>
    <svg class="icon" style="left:126px;top:67px;width:16px;height:16px;color:var(--navy)"><use href="#i-cal"/></svg>
    <div class="label abs" style="left:152px;top:66px">Lorem Ipsum</div>
    <p class="copy abs" style="left:152px;top:72px;width:80px">Lorem ipsum dolor sit amet, consectetur adipiscing elit, sed do eiusmod tempor incididunt ut labore et dolore.</p>
    <svg class="icon" style="left:126px;top:101px;width:16px;height:16px;color:var(--navy)"><use href="#i-doc"/></svg>
    <div class="label abs" style="left:152px;top:100px">Lorem Ipsum</div>
    <p class="copy abs" style="left:152px;top:106px;width:80px">Lorem ipsum dolor sit amet, consectetur adipiscing elit, sed do eiusmod tempor incididunt ut labore et dolore.</p>
  </section>

  <!-- Row 3 -->
  <section class="slide" style="left:64px;top:390px">
    <div class="h" style="position:absolute;left:91px;top:12px">Our Team</div>
    <div class="photo round" role="img" aria-label="Portrait photo of a team member" style="left:22px;top:34px;width:34px;height:34px"></div>
    <div class="tag" style="left:62px;top:36px">Lorem Ipsum</div>
    <p class="copy abs" style="left:62px;top:45px;width:50px">Lorem ipsum dolor sit amet, consectetur adipiscing elit, sed do eiusmod tempor incididunt ut labore et dolore magna aliqua.</p>
    <div class="photo round" role="img" aria-label="Portrait photo of a team member" style="left:133px;top:34px;width:34px;height:34px"></div>
    <div class="tag" style="left:172px;top:36px">Lorem Ipsum</div>
    <p class="copy abs" style="left:172px;top:45px;width:50px">Lorem ipsum dolor sit amet, consectetur adipiscing elit, sed do eiusmod tempor incididunt ut labore et dolore magna aliqua.</p>
    <div class="photo round warm" role="img" aria-label="Portrait photo of a team member" style="left:22px;top:80px;width:34px;height:34px"></div>
    <div class="tag" style="left:62px;top:82px">Lorem Ipsum</div>
    <p class="copy abs" style="left:62px;top:91px;width:50px">Lorem ipsum dolor sit amet, consectetur adipiscing elit, sed do eiusmod tempor incididunt ut labore et dolore magna aliqua.</p>
    <div class="photo round warm" role="img" aria-label="Portrait photo of a team member" style="left:133px;top:80px;width:34px;height:34px"></div>
    <div class="tag" style="left:172px;top:82px">Lorem Ipsum</div>
    <p class="copy abs" style="left:172px;top:91px;width:50px">Lorem ipsum dolor sit amet, consectetur adipiscing elit, sed do eiusmod tempor incididunt ut labore et dolore magna aliqua.</p>
  </section>

  <section class="slide" style="left:348px;top:390px">
    <div class="photo navytint" role="img" aria-label="Photo of a team meeting around a table" style="left:16px;top:0;width:212px;height:62px;opacity:.8"></div>
    <p class="lead abs" style="left:16px;top:88px;width:64px;font-size:5.4px">“Lorem ipsum dolor sit amet, consectetur</p>
    <div class="abs" style="left:16px;top:106px;width:60px;height:.6px;background:var(--navy)"></div>
    <p class="copy abs" style="left:86px;top:74px;width:140px">Lorem ipsum dolor sit amet, consectetur adipiscing elit. Phasellus sodales, ligula ultrices tempus ristique, tellus justo aliquam dui, nec lorem. Lorem ipsum dolor sit amet, consectetur adipiscing elit. Phasellus sodales, ligula ultrices tempus ristique, tellus justo aliquam dui. Lorem ipsum dolor sit amet, consectetur adipiscing elit. Phasellus sodales, ligula ultrices tempus ristique, tellus justo aliquam dui, nec lorem ipsum dolor sit amet. Lorem ipsum dolor sit amet, consectetur adipiscing elit. Phasellus sodales, ligula ultrices tempus ristique.</p>
  </section>

  <section class="slide" style="left:624px;top:390px;background:var(--red-dark)">
    <div class="photo" role="img" aria-label="Dark red tinted photo of a laptop on a desk" style="inset:0;background:linear-gradient(135deg,#7d1914,#c52d25 50%,#8e1c16)"></div>
    <div class="abs" style="left:0;top:30px;width:241px;height:75px;background:rgba(180,36,29,.55)"></div>
    <div class="h white big" style="position:absolute;left:0;width:241px;text-align:center;top:63px">Section Title Here</div>
  </section>

  <section class="slide" style="left:899px;top:390px">
    <div class="abs" style="left:82px;top:0;width:76px;height:136px;background:var(--navy)"></div>
    <p class="quote white abs" style="left:88px;top:26px;width:64px;font-size:5px">“Lorem ipsum dolor sit amet, consectetur adipiscing elit. Phasellus sodales, ligula ultrices tempus ristique, tellus justo aliquam dui,</p>
    <div class="tag navy" style="left:42px;top:26px">Lorem Ipsum</div>
    <p class="copy abs" style="left:20px;top:34px;width:55px;text-align:right">Lorem ipsum dolor sit amet, consectetur adipiscing elit, sed do eiusmod tempor incididunt ut labore et dolore magna aliqua.</p>
    <div class="tag navy" style="left:42px;top:80px">Lorem Ipsum</div>
    <p class="copy abs" style="left:20px;top:88px;width:55px;text-align:right">Lorem ipsum dolor sit amet, consectetur adipiscing elit, sed do eiusmod tempor incididunt ut labore et dolore magna aliqua.</p>
    <div class="tag navy" style="left:172px;top:26px">Lorem Ipsum</div>
    <p class="copy abs" style="left:172px;top:34px;width:55px">Lorem ipsum dolor sit amet, consectetur adipiscing elit, sed do eiusmod tempor incididunt ut labore et dolore magna aliqua.</p>
    <div class="tag navy" style="left:172px;top:80px">Lorem Ipsum</div>
    <p class="copy abs" style="left:172px;top:88px;width:55px">Lorem ipsum dolor sit amet, consectetur adipiscing elit, sed do eiusmod tempor incididunt ut labore et dolore magna aliqua.</p>
  </section>

  <!-- Row 4 -->
  <section class="slide" style="left:64px;top:556px">
    <div class="h" style="position:absolute;left:0;width:241px;text-align:center;top:10px">Edit Title Here</div>
    <div class="photo warm" role="img" aria-label="Photo of a busy desk with laptops from above" style="left:0;top:28px;width:241px;height:52px;opacity:.85"></div>
    <div class="abs" style="left:20px;top:58px;width:56px;height:38px;background:var(--red)"></div>
    <div class="abs" style="left:88px;top:58px;width:56px;height:38px;background:var(--red)"></div>
    <div class="abs" style="left:156px;top:58px;width:56px;height:38px;background:var(--red)"></div>
    <svg class="icon" style="left:42px;top:66px;width:13px;height:13px;color:#fff"><use href="#i-chart"/></svg>
    <svg class="icon" style="left:110px;top:66px;width:13px;height:13px;color:#fff"><use href="#i-doc"/></svg>
    <svg class="icon" style="left:178px;top:66px;width:13px;height:13px;color:#fff"><use href="#i-people"/></svg>
    <div class="label white abs" style="left:20px;width:56px;text-align:center;top:87px">Lorem Ipsum Dolor</div>
    <div class="label white abs" style="left:88px;width:56px;text-align:center;top:87px">Lorem Ipsum Dolor</div>
    <div class="label white abs" style="left:156px;width:56px;text-align:center;top:87px">Lorem Ipsum Dolor</div>
    <p class="copy abs" style="left:20px;top:100px;width:56px;text-align:center">Lorem ipsum dolor sit amet, consectetur adipiscing elit, sed do eiusmod.</p>
    <p class="copy abs" style="left:88px;top:100px;width:56px;text-align:center">Lorem ipsum dolor sit amet, consectetur adipiscing elit, sed do eiusmod.</p>
    <p class="copy abs" style="left:156px;top:100px;width:56px;text-align:center">Lorem ipsum dolor sit amet, consectetur adipiscing elit, sed do eiusmod.</p>
    <div class="mini-brand" style="left:8px;top:127px"><i></i>VORBEK-HALSTRUP</div>
  </section>

  <section class="slide" style="left:348px;top:556px">
    <p class="quote abs" style="left:8px;top:40px;width:44px;font-size:5.6px">“Lorem ipsum dolor sit amet, consectetur adipiscing elit.</p>
    <div class="photo warm" role="img" aria-label="Photo of a smiling woman with glasses at a laptop" style="left:60px;top:0;width:90px;height:136px"></div>
    <svg class="icon" style="left:163px;top:17px;width:9px;height:9px;color:var(--navy)"><use href="#i-lock"/></svg>
    <div class="label abs" style="left:180px;top:16px">Lorem Ipsum Dolor</div>
    <p class="copy abs" style="left:180px;top:22px;width:52px">Lorem ipsum dolor sit amet, consectetur adipiscing elit, sed do eiusmod tempor incididunt ut labore.</p>
    <svg class="icon" style="left:163px;top:57px;width:9px;height:9px;color:var(--navy)"><use href="#i-people"/></svg>
    <div class="label abs" style="left:180px;top:56px">Lorem Ipsum Dolor</div>
    <p class="copy abs" style="left:180px;top:62px;width:52px">Lorem ipsum dolor sit amet, consectetur adipiscing elit, sed do eiusmod tempor incididunt ut labore.</p>
    <svg class="icon" style="left:163px;top:97px;width:9px;height:9px;color:var(--navy)"><use href="#i-down"/></svg>
    <div class="label abs" style="left:180px;top:96px">Lorem Ipsum Dolor</div>
    <p class="copy abs" style="left:180px;top:102px;width:52px">Lorem ipsum dolor sit amet, consectetur adipiscing elit, sed do eiusmod tempor incididunt ut labore.</p>
  </section>

  <section class="slide" style="left:624px;top:556px">
    <div class="photo navytint" role="img" aria-label="Navy-tinted photo of a meeting room" style="left:0;top:0;width:241px;height:60px;background:linear-gradient(135deg,#3a3480,#5a548f 50%,#3a3480)"></div>
    <p class="lead white abs" style="left:20px;top:22px;width:205px;text-align:center;font-weight:400;font-size:5.4px">“Lorem ipsum dolor sit amet, consectetur adipiscing elit. Phasellus sodales, ligula ultrices tempus ristique, tellus justo aliquam dui,</p>
    <svg class="icon" style="left:46px;top:74px;width:18px;height:18px;color:var(--red)"><use href="#i-screen"/></svg>
    <svg class="icon" style="left:112px;top:74px;width:18px;height:18px;color:var(--red)"><use href="#i-doc"/></svg>
    <svg class="icon" style="left:178px;top:74px;width:18px;height:18px;color:var(--red)"><use href="#i-doc"/></svg>
    <div class="label abs" style="left:30px;width:50px;text-align:center;top:98px">Lorem Ipsum</div>
    <div class="label abs" style="left:96px;width:50px;text-align:center;top:98px">Lorem Ipsum</div>
    <div class="label abs" style="left:162px;width:50px;text-align:center;top:98px">Lorem Ipsum</div>
    <p class="copy abs" style="left:28px;top:104px;width:54px;text-align:center">Lorem ipsum dolor sit amet, consectetur adipiscing elit.</p>
    <p class="copy abs" style="left:94px;top:104px;width:54px;text-align:center">Lorem ipsum dolor sit amet, consectetur adipiscing elit.</p>
    <p class="copy abs" style="left:160px;top:104px;width:54px;text-align:center">Lorem ipsum dolor sit amet, consectetur adipiscing elit.</p>
    <div class="mini-brand" style="left:6px;top:127px"><i></i>VORBEK-HALSTRUP</div>
  </section>

  <section class="slide" style="left:899px;top:556px">
    <div class="photo office" role="img" aria-label="Collage of office photos with people at work" style="left:0;top:0;width:135px;height:136px"></div>
    <div class="h" style="position:absolute;left:163px;top:20px;font-size:6px">Lorem Ipsum</div>
    <p class="copy abs" style="left:156px;top:32px;width:80px">Lorem ipsum dolor sit amet, consectetur adipiscing elit, sed do eiusmod tempor incididunt ut labore et dolore magna aliqua. Ut enim ad minim veniam, quis nostrud exercitation ullamco laboris nisi ut aliquip ex ea commodo consequat. Duis aute irure dolor in reprehenderit in voluptate velit esse cillum dolore eu fugiat nulla pariatur. Excepteur sint occaecat cupidatat non proident, sunt in culpa qui officia deserunt mollit anim id est laborum. Lorem ipsum dolor sit amet, consectetur adipiscing elit, sed do eiusmod tempor incididunt ut labore et dolore magna aliqua.</p>
  </section>

  <!-- Row 5 -->
  <section class="slide" style="left:64px;top:716px">
    <div class="photo office" role="img" aria-label="Collage of photos of colleagues working together" style="left:10px;top:12px;width:70px;height:112px"></div>
    <p class="lead abs" style="left:122px;top:22px;width:100px;font-weight:400;font-size:6.4px">Lorem ipsum dolor sit amet, consectetur</p>
    <p class="copy abs" style="left:122px;top:50px;width:100px">Lorem ipsum dolor sit amet, consectetur adipiscing elit. Phasellus sodales, ligula ultrices tempus ristique, tellus justo aliquam dui, nec lorem. Lorem ipsum dolor sit amet, consectetur adipiscing elit. Phasellus sodales, ligula ultrices tempus ristique, tellus justo aliquam dui. Lorem ipsum dolor sit amet, consectetur adipiscing elit. Phasellus sodales, ligula ultrices tempus ristique, tellus justo aliquam dui, nec lorem ipsum dolor sit amet consectetur adipiscing elit phasellus sodales ligula.</p>
    <div class="mini-brand" style="left:8px;top:127px"><i></i>VORBEK-HALSTRUP</div>
  </section>

  <section class="slide" style="left:348px;top:716px">
    <div class="h" style="position:absolute;left:14px;top:12px">Edit Title Here</div>
    <div class="photo city" role="img" aria-label="Photo of a city skyline at dusk with a highway" style="left:16px;top:28px;width:210px;height:62px"></div>
    <svg class="icon" style="left:20px;top:98px;color:var(--red)"><use href="#i-people"/></svg>
    <div class="label red abs" style="left:38px;top:98px">Lorem Ipsum</div>
    <p class="copy abs" style="left:38px;top:104px;width:70px">Lorem ipsum dolor sit amet, consectetur adipiscing elit, sed do eiusmod tempor incididunt ut labore.</p>
    <svg class="icon" style="left:128px;top:98px;color:var(--red)"><use href="#i-play"/></svg>
    <div class="label red abs" style="left:146px;top:98px">Lorem Ipsum</div>
    <p class="copy abs" style="left:146px;top:104px;width:70px">Lorem ipsum dolor sit amet, consectetur adipiscing elit, sed do eiusmod tempor incididunt ut labore.</p>
  </section>

  <section class="slide" style="left:624px;top:716px">
    <div class="abs" style="left:0;top:0;width:241px;height:52px;background:var(--red)"></div>
    <div class="h white" style="position:absolute;left:14px;top:12px;font-size:6.4px">Edit Title Here</div>
    <p class="copy white abs" style="left:14px;top:24px;width:110px">“Lorem ipsum dolor sit amet, consectetur adipiscing elit. Phasellus sodales, ligula ultrices tempus ristique, tellus justo aliquam dui.</p>
    <div class="photo sky" role="img" aria-label="Photo of a waterfront city skyline" style="left:145px;top:20px;width:85px;height:98px"></div>
    <div class="label abs" style="left:14px;top:62px">Lorem ipsum dolor sit amet</div>
    <p class="copy abs" style="left:14px;top:70px;width:122px">Lorem ipsum dolor sit amet, consectetur adipiscing elit. Phasellus sodales, ligula ultrices tempus ristique, tellus justo aliquam dui, nec lorem. Lorem ipsum dolor sit amet, consectetur adipiscing elit. Phasellus sodales, ligula ultrices tempus ristique, tellus justo aliquam dui. Lorem ipsum dolor sit amet, consectetur adipiscing elit. Phasellus sodales, ligula ultrices tempus ristique, tellus justo aliquam dui, nec lorem.</p>
    <div class="mini-brand" style="left:6px;top:127px"><i></i>VORBEK-HALSTRUP</div>
  </section>

  <section class="slide" style="left:899px;top:716px">
    <div class="photo" role="img" aria-label="Photo of hands working on laptops at a shared desk" style="inset:0;background:linear-gradient(135deg,#4b4f6e,#9a9ba6 50%,#d9d6cf)"></div>
    <div class="abs" style="left:0;top:0;width:125px;height:136px;background:var(--navy);opacity:.95"></div>
    <p class="lead white abs" style="left:14px;top:26px;width:105px;font-weight:400;font-size:6.6px">Lorem ipsum dolor sit</p>
    <p class="copy white abs" style="left:14px;top:40px;width:100px">Lorem ipsum dolor sit amet, consectetur adipiscing elit. Phasellus sodales, ligula ultrices tempus ristique, tellus justo aliquam dui, nec lorem. Lorem ipsum dolor sit amet, consectetur adipiscing elit. Phasellus sodales, ligula ultrices tempus ristique, tellus justo aliquam dui. Lorem ipsum dolor sit amet, consectetur adipiscing elit. Phasellus sodales, ligula ultrices tempus ristique, tellus justo aliquam dui, nec lorem ipsum dolor sit amet consectetur adipiscing.</p>
  </section>

  <!-- Row 6 -->
  <section class="slide" style="left:64px;top:882px">
    <div class="h" style="position:absolute;left:14px;top:12px">Edit Title Here</div>
    <div class="photo navytint" role="img" aria-label="Navy-tinted photo background" style="left:17px;top:30px;width:64px;height:90px"></div>
    <div class="photo redtint" role="img" aria-label="Red-tinted photo background" style="left:88px;top:30px;width:64px;height:90px"></div>
    <div class="photo navytint" role="img" aria-label="Navy-tinted photo background" style="left:160px;top:30px;width:64px;height:90px"></div>
    <svg class="icon" style="left:42px;top:48px;width:14px;height:14px;color:#fff"><use href="#i-cal"/></svg>
    <svg class="icon" style="left:113px;top:48px;width:14px;height:14px;color:#fff"><use href="#i-screen"/></svg>
    <svg class="icon" style="left:185px;top:48px;width:14px;height:14px;color:#fff"><use href="#i-down"/></svg>
    <div class="label white abs" style="left:17px;width:64px;text-align:center;top:78px">LOREM IPSUM DOLOR</div>
    <div class="label white abs" style="left:88px;width:64px;text-align:center;top:78px">LOREM IPSUM DOLOR</div>
    <div class="label white abs" style="left:160px;width:64px;text-align:center;top:78px">LOREM IPSUM DOLOR</div>
    <p class="copy white abs" style="left:22px;top:86px;width:54px;text-align:center">Lorem ipsum dolor sit amet, consectetur adipiscing elit, sed do eiusmod tempor.</p>
    <p class="copy white abs" style="left:93px;top:86px;width:54px;text-align:center">Lorem ipsum dolor sit amet, consectetur adipiscing elit, sed do eiusmod tempor.</p>
    <p class="copy white abs" style="left:165px;top:86px;width:54px;text-align:center">Lorem ipsum dolor sit amet, consectetur adipiscing elit, sed do eiusmod tempor.</p>
  </section>

  <section class="slide" style="left:350px;top:882px">
    <div class="abs" style="left:0;top:0;width:126px;height:136px;background:var(--navy-deep)"></div>
    <p class="lead white abs" style="left:16px;top:20px;width:100px;font-weight:400;font-size:6.4px">Lorem ipsum dolor sit amet, consectetur</p>
    <p class="copy white abs" style="left:16px;top:44px;width:100px">Lorem ipsum dolor sit amet, consectetur adipiscing elit. Phasellus sodales, ligula ultrices tempus ristique, tellus justo aliquam dui, nec lorem. Lorem ipsum dolor sit amet, consectetur adipiscing elit. Phasellus sodales, ligula ultrices tempus ristique, tellus justo aliquam dui. Lorem ipsum dolor sit amet, consectetur adipiscing elit. Phasellus sodales, ligula ultrices tempus ristique, tellus justo aliquam dui, nec lorem ipsum dolor sit amet.</p>
    <svg class="icon" style="left:142px;top:20px;color:var(--navy)"><use href="#i-people"/></svg>
    <div class="label abs" style="left:164px;top:18px">Lorem Ipsum</div>
    <p class="copy abs" style="left:164px;top:24px;width:66px">Lorem ipsum dolor sit amet, consectetur adipiscing elit, sed do eiusmod tempor incididunt ut labore et dolore.</p>
    <svg class="icon" style="left:142px;top:60px;color:var(--navy)"><use href="#i-truck"/></svg>
    <div class="label abs" style="left:164px;top:58px">Lorem Ipsum</div>
    <p class="copy abs" style="left:164px;top:64px;width:66px">Lorem ipsum dolor sit amet, consectetur adipiscing elit, sed do eiusmod tempor incididunt ut labore et dolore.</p>
    <svg class="icon" style="left:142px;top:98px;color:var(--navy)"><use href="#i-play"/></svg>
    <div class="label abs" style="left:164px;top:96px">Lorem Ipsum</div>
    <p class="copy abs" style="left:164px;top:102px;width:66px">Lorem ipsum dolor sit amet, consectetur adipiscing elit, sed do eiusmod tempor incididunt ut labore et dolore.</p>
  </section>

  <section class="slide" style="left:624px;top:882px">
    <p class="quote abs" style="left:8px;top:38px;width:44px;font-size:5.4px;text-align:left">“Lorem ipsum dolor sit amet, consectetur adipiscing</p>
    <div class="abs" style="left:56px;top:0;width:105px;height:136px;background:var(--red)"></div>
    <div class="label white abs" style="left:68px;top:16px">Lorem Ipsum Dolor</div>
    <p class="copy white abs" style="left:68px;top:22px;width:50px">Lorem ipsum dolor sit amet, consectetur adipiscing elit, sed do eiusmod tempor incididunt.</p>
    <div class="label white abs" style="left:68px;top:56px">Lorem Ipsum Dolor</div>
    <p class="copy white abs" style="left:68px;top:62px;width:50px">Lorem ipsum dolor sit amet, consectetur adipiscing elit, sed do eiusmod tempor incididunt.</p>
    <div class="label white abs" style="left:68px;top:96px">Lorem Ipsum Dolor</div>
    <p class="copy white abs" style="left:68px;top:102px;width:50px">Lorem ipsum dolor sit amet, consectetur adipiscing elit, sed do eiusmod tempor incididunt.</p>
    <div class="photo" role="img" aria-label="Photo of hands holding a tablet in front of a monitor" style="left:128px;top:0;width:113px;height:136px;background:linear-gradient(135deg,#c9ced8,#8d93a3 50%,#5e6272)"></div>
  </section>

  <section class="slide" style="left:899px;top:882px">
    <div class="photo navytint" role="img" aria-label="Navy-tinted photo looking up at skyscrapers" style="inset:0;background:linear-gradient(160deg,#252058,#4c5590 45%,#2b2667)"></div>
    <div class="h white" style="position:absolute;left:0;width:241px;text-align:center;top:36px;font-size:11.5px">Thank You</div>
    <div class="abs" style="left:72px;top:57px;width:98px;height:.6px;background:#fff"></div>
    <div class="label white abs" style="left:0;width:241px;text-align:center;top:65px;font-size:4.4px">Company Name</div>
    <p class="copy white abs" style="left:70px;top:78px;width:100px;text-align:center;font-size:3.4px;font-weight:600">12 Strandgade Allé,<br>1401 København K</p>
    <p class="copy white abs" style="left:50px;top:95px;width:140px;text-align:center;font-size:3.2px;font-weight:600">P: +45 00 00 00 00 &nbsp;•&nbsp; W: www.vorbek-halstrup.com</p>
  </section>

</main>
</body>
</html>
```